Trifold Brochure

This is relatively easy. We already have a trifold made we simply want to update the LOOK to look more like our current website. All content would stay the same the only thing that would change would be the fonts, colors and background images to match the current website.

I have attached a word doc of the old trifold brochure. We would want the content to remain on the same pages of the trifold. Again all you are doing is updating the font, logo, colors and any background images. Please comment with any questions.

This is a 5 day project!

Requirements
Must have
• Logo, colors and fonts to match our current website.
http://www.brackenfieldworks.example/

```html
<!DOCTYPE html>
<html lang="en">
<head>
<meta charset="utf-8">
<title>Piling System Trifold</title>
<link rel="stylesheet" href="https://fonts.googleapis.com/css2?family=Questrial&family=Nunito:ital,wght@1,400;1,600;1,700&display=swap">
<style>
  :root {
    --band-light: #b9c89d;
    --band-dark: #5e7737;
    --band-mid: #6f8a49;
    --ink: #2b2b2b;
    --accent: #6b7f3e;
    --wood-ink: #6a7a2c;
    --wood-a: #e9cfa6;
    --wood-b: #dcb88a;
    --panel-green: #dfe8cf;
    --white: #ffffff;
  }
  html, body { margin: 0; padding: 0; overflow: hidden; }
  body { width: 1200px; height: 927px; background: var(--white); }
  .brochure { position: relative; width: 1200px; height: 927px; overflow: hidden; font-family: "Questrial", sans-serif; color: var(--ink); }

  .top-band { position: absolute; left: 0; top: 0; width: 1200px; height: 75px; background: var(--band-light); }
  .top-arc { position: absolute; left: 0; top: 0; }

  .left-backdrop { position: absolute; left: 0; top: 108px; width: 398px; height: 775px;
    background: linear-gradient(90deg, #cfdcb8 0%, var(--panel-green) 40%, #eef3e6 100%); }
  .left-sheet { position: absolute; left: 108px; top: 108px; width: 290px; height: 775px; background: var(--white); }
  .right-backdrop { position: absolute; left: 805px; top: 108px; width: 395px; height: 775px;
    background: linear-gradient(180deg, #ffffff 0%, #ffffff 70%, #f2f5ec 100%); }

  .wood-panel { position: absolute; left: 398px; top: 20px; width: 407px; height: 863px;
    background: linear-gradient(100deg, var(--wood-a) 0%, #f0dcb8 35%, var(--wood-b) 70%, #e6c69a 100%); }
  .wood-stitch { position: absolute; left: 398px; width: 407px; border-top: 2px dashed #8a9a4a; opacity: .7; }

  .header-bar { position: absolute; top: 68px; height: 40px; background: var(--band-dark); color: var(--white);
    font-size: 16.5px; line-height: 20px; box-sizing: border-box; }
  .header-bar.left { left: 0; width: 398px; text-align: right; padding: 9px 30px 0 0; }
  .header-bar.right { left: 805px; width: 395px; padding: 2px 0 0 18px; }

  .bottom-bar { position: absolute; left: 0; top: 883px; width: 1200px; height: 44px; background: var(--band-dark); }
  .bottom-bar .mid { position: absolute; left: 398px; width: 407px; height: 44px; background: var(--band-mid); }

  .includes { position: absolute; left: 130px; top: 124px; width: 238px; font-size: 15.5px; line-height: 22px; }
  .includes ul { list-style: none; margin: 0; padding: 0; }
  .includes li { text-align: justify; margin-bottom: 20px; }
  .includes h3 { font-weight: 400; font-size: 15.5px; color: var(--accent); margin: -4px 0 0; line-height: 22px; }
  .includes p { margin: 0; }

  .story { position: absolute; left: 421px; top: 42px; width: 362px; font-family: "Nunito", sans-serif; font-style: italic;
    color: var(--wood-ink); font-size: 12.6px; line-height: 16.4px; text-align: justify; }
  .story .lead { font-size: 22px; font-weight: 600; letter-spacing: .2px; }
  .story p { margin: 0; }
  .story h3 { font-size: 12.8px; font-weight: 700; margin: 14px 0 1px; }

  .standards { position: absolute; left: 823px; top: 124px; width: 355px; font-size: 14.2px; line-height: 18.8px; letter-spacing: -0.1px; }
  .standards ol { margin: 0; padding: 0; list-style: none; }
  .standards li { margin-bottom: 17px; text-align: justify; }
  .standards li:last-child { margin-bottom: 6px; }
  .standards .sub { padding-left: 36px; }
  .contact { display: block; text-align: center; font-style: normal; margin-left: -18px; width: 391px; }
</style>
</head>
<body>
<div class="brochure">
  <div class="top-band" role="img" aria-label="Light green diagonal pattern band"></div>
  <svg class="top-arc" width="1200" height="75" viewBox="0 0 1200 75" aria-hidden="true">
    <path d="M0 70 Q600 -40 1200 70 L1200 75 L0 75 Z" fill="#ffffff"/>
    <path d="M0 70 Q600 -40 1200 70" fill="none" stroke="#3e4f22" stroke-width="2"/>
  </svg>

  <div class="left-backdrop" role="img" aria-label="Faint green architectural floor plan drawing"></div>
  <div class="left-sheet"></div>
  <div class="right-backdrop"></div>
  <div class="wood-panel" role="img" aria-label="Light wood grain texture"></div>
  <div class="wood-stitch" style="top:861px"></div>
  <div class="wood-stitch" style="top:866px"></div>

  <div class="header-bar left">Our System includes:</div>
  <div class="header-bar right">General Performance Standards,<br>Notes and Guidance:</div>
  <div class="bottom-bar"><div class="mid"></div></div>

  <section class="includes">
    <ul>
      <li>• Collar cut to customer length in sizes ranging from 12” to 144”.</li>
      <li>• Collar Cap with galvanized steel u-bolts to connect to the structure.</li>
      <li>• Collar spacers to allow for variations in Piling diameter.</li>
      <li>• Collar Cap spacers to allow for variations in Piling diameter.</li>
      <li>• Tubes of high strength adhesive glue to connect the Piling to the Collar and for the Collar flange and to fill gaps between the Piling and the Collar due to the nature of irregular Pilings.</li>
      <li>• Detailed installation manual providing guidance to the installation contractor.</li>
      <li>• Detailed written specifications provided in paper format and available in word format upon request.</li>
    </ul>
    <h3>Flexibility:</h3>
    <p>Our system has been designed to accommodate piles ranging in diameter from 8” to 12”. The system can also correct vertical alignments by up to 6 degrees.</p>
  </section>

  <section class="story">
    <p><span class="lead">Our Patented Piling system</span> has been designed to withstand the corrosive environment of beach communities. The salt water and windblown sand corrodes unprotected materials, and yes, even stainless steel. Our system utilizes a high strength carbon fiber material that is corrosion proof from salt water and UV proof. The system will not erode, decay or loose strength over time. The system has three installation conditions, for raising a house on existing pilings, repairing damaged pilings, and for connecting new pilings to floor joists in new construction. The three options are generally described below:</p>
    <h3>RAISING A STRUCTURE</h3>
    <p>A house on pilings can be raised by disconnecting the house from the pilings, raise the house to create a work area, cut all of the piles to a preset elevation, and install the Collar on the piling. The Collar is connected to the piling by six galvanized lag bolts and is glued with a high strength adhesive and all gaps are filled with flowable epoxy fill and fiber. The Collar extends above the piling to the bottom of the home’s joists to the preset height, up to 6’-6”, or higher when lateral supports are considered. Once the Collar is set on the home, it is filled with concrete to transfer the load of the house from the floor joists directly to the top of the piling, the concrete provides the compressive strength, while the Collar provides tensile and shear strength.<br>A Collar Cap is then installed with two galvanized steel u-bolts which extend into the floor joists for the installer to connect to the joists.</p>
    <h3>PILING REPAIRS AND EXTENSIONS</h3>
    <p>A 36” section of Collar can be installed onto an existing piling and a new section of piling can be placed on top, with 18” of the Collar covering the top of the existing and 18” covering the bottom of the new piling. Generally, the minimum length of the new piling needs to be 6 feet to ensure the piling length is not too short, which could lead to reduced piling loading capacity. This option generally requires lateral support of the pilings. Consult with your design professional</p>
    <h3>NEW CONSTRUCTION</h3>
    <p>The standard practice for connecting pilings to floor joists is to notch the pilings and bolt the joists to the pilings. This method dramatically reduces the strength of the piling due to reduced cross sectional area at the connection point. Additionally, this connection method exposes more surface area of the piling allowing for additional potential for dry rot. A 12” Collar section with a Collar Cap can be used to connect directly to the top of the new piling providing a connection that will outlast the piling by literally thousands of years.</p>
  </section>

  <section class="standards">
    <ol>
      <li>1.&nbsp;&nbsp; General Performance Standards:
        <div class="sub">a. Vertical loading (vertical compression) 90 Kips<br>b. Bending moment 65 ft-Kips<br>c. Shear (lateral forces) 10 Kips.<br>d. Alignment/plumpness correction 6 Deg.</div></li>
      <li>2. This document and information provided is the property of BFW and shall not be altered, used or referenced by any third party without the expressed written permission of BFW.</li>
      <li>3. The User of this system is advised that they should obtain services of a design professional for the use of this product. BFW only represents that our product will withstand loading as documented in our specifications. The design professional shall evaluate the loading conditions and determine if the loading conditions fall within the parameters of the Collar system. Additionally, the user should employ the design professional to inspect the Pilings to ensure they are acceptable for use.</li>
      <li>4. Local Permitting may be required for use of this product. Consult with your local code official prior to use.</li>
      <li>5. The User of this system should employ installation contractors that have adequate skills for the required work. BFW does not and cannot attest to any skill set or quality of work of any installer.</li>
      <li>6. The written instructions for installation must be followed. Failure to do so could result in failure of the system.</li>
    </ol>
    <address class="contact">
      PO Box 41580,<br>Millbrook Ridge, PA 18099-0041<br>T. 610. 555.0142 &nbsp;• F. 610.555.0187<br>Email: sales@brackenfieldworks.example<br>www.brackenfieldworks.example
    </address>
  </section>
</div>
</body>
</html>
```